Banner Ad Design Project

I need a banner design. The website is under construction at www.brightmarrow.example

Name: Bright Marrow
Tagline: Steady Sparks for crowded calendars

This is a leadership development and executive coaching site. The past site is live at www.quillstepnow.example. (so you can get a sense of the content)

The audience are (BUSY) executives, senior managers, leaders and top professionals, so the feel needs to be highly professional but also modern and fresh. I want to communicate energy but also solid and trust worthy and not too new agey. The audience are also people with strong social values who want to change things - so not too corporate (Ie suits!)

I would like the design to be floating on a white background, very clean and simple. I am attracted to reds or sunset (burn orange crimson colors.) But totally open to any color ideas.
I am giving an open brief for your ideas.
Here are the dimensions 960px wide, roughly 190px height.

Reason: The weekend might give more time to designers to get involved. Thanks Vina

Hi designers

You may not have seen the additions I gave to this brief.

The banner should not have leader out front photo's. Maybe less corporate than I initially thought. 
Not too corporate (no suits!) Please no chess pieces, jigsaw pieces, cartoon images, cliche leadership images. 
Am am trying for inspiration /inspiring whilst still being professional. Very simple and clean.
Please can the design be floating in a white background so that the web page is borderless - A bit like it is in http://palmoriskel.example/
Thank you

Target Market(s)

Senior managers, executives but people who also want to change the world!

Industry/Entity Type

Construction

Requirements
Should not have
• Should not have leader out front photo's.
Maybe less corporate than I initially thought.
Am am trying for inspiration /inspiring whilst still being professional.
Please no chess pieces, jigsaw pieces, cartoon images, cliche leadership images. Not too corporate (Ie suits!)

Thanks

```html
<!DOCTYPE html>
<html lang="en">
<head>
<meta charset="utf-8">
<title>Bright Marrow — Steady Sparks for crowded calendars</title>
<link rel="stylesheet" href="https://fonts.googleapis.com/css2?family=Lora:wght@400&display=swap">
<style>
  :root {
    --sky-deep: #3eb2d8;
    --sky-mid: #8fd3e6;
    --mist: #c9e9ea;
    --spring: #cfe7a6;
    --leaf: #9fd04a;
    --leaf-deep: #6fae2c;
    --ink: #2a2a6e;
    --ghost-word: rgba(70, 110, 150, 0.22);
    --band: rgba(255, 255, 255, 0.45);
  }
  html, body {
    margin: 0;
    padding: 0;
    overflow: hidden;
    background: #ffffff;
  }
  .banner {
    position: relative;
    width: 1200px;
    height: 238px;
    overflow: hidden;
    background: linear-gradient(90deg,
      var(--sky-deep) 0%,
      var(--sky-mid) 32%,
      var(--mist) 55%,
      var(--spring) 78%,
      #d6ec9a 100%);
    font-family: "Lora", Georgia, serif;
  }
  .ghost-word {
    position: absolute;
    margin: 0;
    color: var(--ghost-word);
    font-weight: 400;
    line-height: 1;
    white-space: nowrap;
  }
  .ghost-word--top {
    left: 520px;
    top: -14px;
    font-size: 74px;
  }
  .ghost-word--bottom {
    left: -6px;
    top: 150px;
    font-size: 128px;
    color: rgba(60, 120, 160, 0.16);
  }
  .tagline-band {
    position: absolute;
    left: 0;
    top: 100px;
    width: 900px;
    height: 52px;
    background: linear-gradient(90deg, var(--band) 0%, var(--band) 70%, rgba(255,255,255,0) 100%);
  }
  .brand-name {
    position: absolute;
    left: 52px;
    top: 28px;
    margin: 0;
    font-size: 46px;
    font-weight: 400;
    color: var(--ink);
    line-height: 1;
  }
  .tagline {
    position: absolute;
    left: 144px;
    top: 107px;
    margin: 0;
    font-size: 31px;
    font-weight: 400;
    color: var(--ink);
    line-height: 1.2;
    white-space: nowrap;
  }
  .leaf-spray {
    position: absolute;
    right: 0;
    top: 0;
    width: 420px;
    height: 238px;
    background:
      radial-gradient(ellipse 38% 42% at 35% 30%, rgba(159, 208, 74, 0.9) 0%, rgba(159, 208, 74, 0) 100%),
      radial-gradient(ellipse 34% 40% at 62% 62%, rgba(111, 174, 44, 0.85) 0%, rgba(111, 174, 44, 0) 100%),
      radial-gradient(ellipse 30% 30% at 85% 15%, rgba(200, 230, 120, 0.7) 0%, rgba(200, 230, 120, 0) 100%);
  }
</style>
</head>
<body>
  <header class="banner">
    <p class="ghost-word ghost-word--top" aria-hidden="true">Inspiration</p>
    <p class="ghost-word ghost-word--bottom" aria-hidden="true">Leadership</p>
    <div class="leaf-spray" role="img" aria-label="Sprig of fresh green maple leaves against a soft, sunlit green background"></div>
    <div class="tagline-band"></div>
    <h1 class="brand-name">Bright Marrow</h1>
    <p class="tagline">Steady Sparks for crowded calendars</p>
  </header>
</body>
</html>
```